TLW Facebook Page Cover Image

I am setting up a Facebook company page for my new business called 'TidewaterLinkWorks'. We provide business owners, executives, and managers with valuable information via a comprehensive suite of employee assessment products to make better people decisions. Company tagline is Staff Smarter - Grow Teams - Reach Targets. I need a attention grabbing, polished, professional cover graphic to be displayed on the top of the page that captures who we are and is a nice compliment to our logo which will appear in the smaller logo box. Company personality is contemporary, energetic, competent yet humble. Logo is attached. Please view our 3 minute overview video on YouTube to get a sense of who we are/what we do. https://www.examplevideohost.net/watch?v=Qor7mTa2LpW

Target Market(s)

My website is a B2B website. My ideal "sweet spot" client company employees approximately 200-300 employees, although my secondary products and service market will include companies above 200-300 employees to include select Fortune 500 companies. Target client roles within these companies include:
- Business Leaders - CEO's, Presidents, and General Managers
- Small & Mid-sized business owners
- Functional Leaders - CFOs, CIO, Sales/Marketing leaders, HR leaders
- Functional Specialists - Recruiting, Learning & Development, OD
- 1st and 2nd line managers
Our products and services can be used effectively across all industries, but if I had to pick the top 5 or 6 "target" industries or type of businesses that match extremely well to our products/services I'd say retail/consumer products, healthcare/human services, direct/outside sales (*e.g. car dealers, medical equipment sales, telemarketing, etc.), customer service call centers, hospitality, and banking.

Industry/Entity Type

Business

Font styles to use
Sans Serif

Requirements
Nice to have
• Don't want the graphic to be too busy or crowded. Photography and/or from scratch graphics can be used separately or in combination. Attached is a sample from an unrelated web page I like in terms of it's white space/graphic/text balance.

```html
<!DOCTYPE html>
<html lang="en">
<head>
<meta charset="utf-8">
<title>TidewaterLinkWorks – Cover</title>
<link rel="stylesheet" href="https://fonts.googleapis.com/css2?family=Parisienne&family=Roboto+Condensed:wght@400&display=swap">
<style>
  :root {
    --deep-blue: #0a1f7a;
    --royal-blue: #1838b8;
    --bright-blue: #2c5ce0;
    --globe-dark: #1b2f6e;
    --globe-light: #6f8fc4;
    --gold-dark: #a27b2c;
    --gold-light: #f0d98a;
    --script-white: #ffffff;
    --rule-light: rgba(220, 230, 255, 0.7);
    --rule-faint: rgba(220, 230, 255, 0.45);
    --tag-text: #c5cbe0;
  }
  * { margin: 0; padding: 0; box-sizing: border-box; }
  html, body { width: 1200px; height: 444px; overflow: hidden; background: var(--deep-blue); }
  .cover {
    position: relative;
    width: 1200px;
    height: 444px;
    overflow: hidden;
  }
  .world-backdrop {
    position: absolute;
    inset: 0;
    background:
      radial-gradient(ellipse 520px 300px at 330px 250px, rgba(80,130,240,0.55), transparent 70%),
      radial-gradient(ellipse 380px 260px at 820px 360px, rgba(60,110,230,0.45), transparent 70%),
      linear-gradient(100deg, var(--deep-blue) 0%, var(--royal-blue) 45%, var(--bright-blue) 75%, var(--royal-blue) 100%);
  }
  .globe {
    position: absolute;
    left: 910px;
    top: -42px;
    width: 352px;
    height: 352px;
    border-radius: 50%;
    background: radial-gradient(circle at 35% 40%, var(--globe-light) 0%, #3f5f9c 45%, var(--globe-dark) 80%);
    box-shadow: 0 0 60px rgba(200,220,255,0.35);
  }
  .partner-badge {
    position: absolute;
    left: 11px;
    top: 10px;
    width: 203px;
    height: 61px;
    border: 2px solid #e7cf7d;
    background: linear-gradient(135deg, var(--gold-light), var(--gold-dark) 60%, var(--gold-light));
  }
  .frame-lines { position: absolute; inset: 0; }
  .slogan {
    position: absolute;
    inset: 0;
    font-family: "Parisienne", cursive;
    color: var(--script-white);
    font-size: 64px;
    line-height: 1;
  }
  .slogan span { position: absolute; white-space: nowrap; text-shadow: 0 1px 3px rgba(0,0,40,0.5); }
  .slogan .word-one { left: 28px; top: 130px; }
  .slogan .word-two { left: 386px; top: 174px; }
  .slogan .word-three { left: 618px; top: 212px; }
  .tagline {
    position: absolute;
    inset: 0;
    font-family: "Roboto Condensed", sans-serif;
    font-size: 13px;
    letter-spacing: 0.3px;
    color: var(--tag-text);
    text-transform: uppercase;
  }
  .tagline span { position: absolute; white-space: nowrap; }
  .tagline .step-three { left: 1061px; top: 306px; }
  .tagline .step-two { left: 996px; top: 356px; }
  .tagline .step-one { left: 933px; top: 404px; }
</style>
</head>
<body>
  <div class="cover">
    <div class="world-backdrop" role="img" aria-label="Blue world map with glowing network connection lines"></div>
    <div class="globe" role="img" aria-label="Globe with latitude and longitude grid"></div>
    <div class="partner-badge" role="img" aria-label="Partner badge"></div>

    <svg class="frame-lines" width="1200" height="444" viewBox="0 0 1200 444" aria-hidden="true">
      <g stroke="var(--rule-faint)" stroke-width="1.2" fill="none">
        <line x1="926" y1="0" x2="926" y2="444"/>
        <line x1="983" y1="0" x2="983" y2="444"/>
        <line x1="1054" y1="0" x2="1054" y2="444"/>
        <line x1="1100" y1="0" x2="1100" y2="444"/>
        <line x1="1129" y1="0" x2="1129" y2="444"/>
        <line x1="1154" y1="0" x2="1154" y2="444"/>
        <line x1="1181" y1="0" x2="1181" y2="444"/>
        <line x1="384" y1="190" x2="1200" y2="190"/>
        <line x1="614" y1="233" x2="983" y2="233"/>
        <line x1="900" y1="271" x2="1054" y2="271"/>
      </g>
      <g stroke="var(--rule-light)" stroke-width="1.5">
        <line x1="48" y1="192" x2="384" y2="192"/>
        <line x1="384" y1="234" x2="616" y2="234"/>
        <line x1="616" y1="273" x2="900" y2="273"/>
        <line x1="1054" y1="324" x2="1181" y2="324"/>
        <line x1="983" y1="374" x2="1110" y2="374"/>
        <line x1="926" y1="422" x2="1016" y2="422"/>
      </g>
    </svg>

    <div class="slogan">
      <span class="word-one">”Demonstration</span>
      <span class="word-two">Outweighs</span>
      <span class="word-three">Presentation”</span>
    </div>

    <div class="tagline">
      <span class="step-three">Reach Targets</span>
      <span class="step-two">Grow Teams</span>
      <span class="step-one">Staff Smarter</span>
    </div>
  </div>
</body>
</html>
```